Banner for top of wordpress website

Open to ideas but no images relating to people, or cars or numbers.

Modern, clean design.

Fonts- see logo and fonts on page 1 attached document.

Lots of white space. 

Corporate colors red and black. OK to bring in other color if appropriate such as grey.  See attached business cards for color. 

Imagary abstract but relating to our business which is engagement (and social media) marketing.

Target Market(s)

Corporates and small to medium size businesses looking to better utilize social media and online and offline channels in order to better serve and educate their customers and ultimately find new customers (through an educational process that focuses on the longer term development of a relationship).

Industry/Entity Type

Publishing

Number of Pages Required

1 page

Requirements
Must have
• Please include the following in your design:
• • An image or graphic for the first page of the website.
• • Selection of appropriate typeface that is able to be used in Wordpress for accompanying text on site.

```html
<!DOCTYPE html>
<html lang="en">
<head>
<meta charset="utf-8">
<title>Further Media — Home</title>
<link rel="stylesheet" href="https://fonts.googleapis.com/css2?family=Jost:wght@400;500;700&family=Inter:wght@400;600&display=swap">
<style>
  :root {
    --paper: #eceeed;
    --band: #a9abae;
    --brand-red: #c4103f;
    --ink: #1b1b1b;
    --white: #ffffff;
    --hero-light: #a3a3a1;
    --hero-dark: #6f706e;
  }
  * { margin: 0; padding: 0; box-sizing: border-box; }
  html, body { width: 1200px; height: 840px; overflow: hidden; background: var(--paper); }
  body { position: relative; font-family: "Inter", Arial, sans-serif; color: var(--ink); }

  .site-header { position: absolute; left: 216px; top: 56px; display: flex; align-items: center; gap: 12px; }
  .brand-mark { width: 34px; height: 34px; background: var(--brand-red); }
  .brand-name { font-family: "Jost", sans-serif; font-weight: 500; font-size: 34px; letter-spacing: 0.2px; color: var(--ink); line-height: 1; }

  .main-nav { position: absolute; left: 216px; top: 134px; width: 748px; height: 50px; background: var(--band); }
  .main-nav ul { list-style: none; display: flex; height: 100%; align-items: center; padding-left: 16px; gap: 17px; }
  .main-nav a { font-family: "Inter", Arial, sans-serif; font-size: 13px; letter-spacing: 2.2px; color: var(--white); text-decoration: none; padding-bottom: 3px; }
  .main-nav a.is-current { border-bottom: 2px solid var(--white); }

  .hero { position: absolute; left: 216px; top: 197px; width: 748px; height: 200px; overflow: hidden; }
  .hero-photo { position: absolute; inset: 0; background: linear-gradient(90deg, var(--hero-light) 0%, #8f908e 30%, var(--hero-dark) 100%); }
  .hero-copy { position: absolute; left: 256px; top: 22px; color: var(--white); font-family: "Jost", sans-serif; }
  .hero-title { font-weight: 700; font-size: 42px; line-height: 48px; letter-spacing: 1.6px; text-transform: uppercase; }
  .hero-sub { margin-top: 10px; font-weight: 500; font-size: 23px; line-height: 29px; }

  .divider { position: absolute; left: 216px; top: 409px; width: 748px; height: 12px; background: var(--band); }

  .features { position: absolute; left: 216px; top: 448px; width: 748px; display: flex; gap: 22px; }
  .feature { width: 235px; }
  .feature h2 { font-family: "Inter", Arial, sans-serif; font-weight: 400; font-size: 16px; line-height: 22.5px; color: var(--brand-red); text-transform: uppercase; letter-spacing: 0.2px; }
  .feature p { margin-top: 9px; font-size: 9.5px; line-height: 15.5px; color: var(--ink); }
  .feature p a { color: var(--brand-red); text-decoration: none; }
  .read-more { display: inline-block; margin-top: 15px; font-weight: 600; font-size: 10.5px; color: var(--brand-red); text-decoration: none; }
  .feature--mid .read-more { margin-top: 5px; }
  .feature--right .read-more { margin-top: 5px; }

  .site-footer { position: absolute; left: 216px; top: 711px; width: 746px; border-top: 6px solid var(--band); padding-top: 7px; font-size: 7px; letter-spacing: 0.6px; text-transform: uppercase; color: var(--ink); }
</style>
</head>
<body>
  <header class="site-header">
    <span class="brand-mark" aria-hidden="true"></span>
    <span class="brand-name">further media</span>
  </header>

  <nav class="main-nav">
    <ul>
      <li><a class="is-current" href="#">HOME</a></li>
      <li><a href="#">PORTFOLIO</a></li>
      <li><a href="#">SERVICES</a></li>
      <li><a href="#">ABOUT</a></li>
      <li><a href="#">CONTACT</a></li>
    </ul>
  </nav>

  <section class="hero">
    <div class="hero-photo" role="img" aria-label="Black and white photograph of a man pushing a scooter along a road beside a concrete wall"></div>
    <div class="hero-copy">
      <h1 class="hero-title">Are you getting<br>enough mileage?</h1>
      <p class="hero-sub">Learn how Further Media gets you more<br>&nbsp;from your engagement marketing strategy</p>
    </div>
  </section>

  <div class="divider"></div>

  <main class="features">
    <article class="feature">
      <h2>Information to transform your life</h2>
      <p>Cus am, quis volorrorerum il ium asincidero dolorio el invel mos dolorpor moluptatus. Ferit, que natur? Qui consequi blabore henim menimagni qui officitatur ad ute nessequei,Qui consequi blabore henim sunt, ut harum volut nescia qui ra aut evel invel mos dolorpor moluptatus. Ferit, que natur? Qui consequi <a href="#">blabore</a> henimi, sunt, ut harum volut doluptaecea comnienda num rem et, ommolup tatio. Ut quia <a href="#">que et eatis</a> utecullaut</p>
      <a class="read-more" href="#">Read More...</a>
    </article>
    <article class="feature feature--mid">
      <h2>More from your digital marketing strategy</h2>
      <p>Maximporro voluptiam isiminc ilibus explis ea doloreresto mo volorrovit est ut adio blaccuel invel mos dolorpor moluptatus. Ferit, que natur? Qui consequi blabore henimi, sunt, ut harum volut doluptaecm iumenimagni qui officitatur veni rem qui dolorum conserro eos et aut aut as ut omnis enda Qui consequi blabore henim andeni cmenimagni qui officitatur ea doloreresto mo ad ute nessequeonsed quis corio <a href="#">quasperem</a> rrorerumcidero</p>
      <a class="read-more" href="#">Read More...</a>
    </article>
    <article class="feature feature--right">
      <h2>Increase your profile and influence</h2>
      <p>Tdoloreresto mo volorrovit est ut adio blaccum iumenimagni qui officitatur ad ute nel invel mos dolorpor moluptatus. Ferit, que natur? Qui consequi loremiop menimagni qui officitatur ad ute nesse queblabore <a href="#">henimi, sun</a>t, ut harum volut doluptaecesseque veni rem qui dolorum conserro eos et aut aut as ut omnis enda andeni consed quis corio quasperem Cus am, quis <a href="#">volorrorerum il</a> ium asincidero dolorio rehenimin nescia <a href="#">qui ra aut</a> loremam, quis</p>
      <a class="read-more" href="#">Read More...</a>
    </article>
  </main>

  <footer class="site-footer">Copyright © 2009 · All rights reserved · Further Media · Site Admin</footer>
</body>
</html>
```